Website Wordpress Responsive Design and Development - Landscape Company

Site is currently under construction, but the old site needs a refresh.
Need a fully responsive wordpress website (built in Elementor or comparable theme).
Here's the way it looked prior :
https://pastpages.example/snap/20220330041341/http://brookmoorgreens.example/
Their current designer came up with a website sample and it looks terrible :
https://talkowenpics.sitebuild.example/mysite/projects
Websites the client likes for some inspiration, but needs better than these :
https://www.quarrinbeckgroundworkers.example/
http://kvatelierpx.example/
https://tullidgepartners.example/
https://www.garbettcoinc.example/

Navigation includes :
• Home
• Complete structure of website content is available in the home page, yielding main information on services.
• Visually appealing but simple to use and navigate. Subtle amount of content, but enough for search engines to be able to read up the target phrases.
• Sections on the home page include :
▪ About - Information about the company and main service focus
▪ Gallery - Imagery categorized to include lightbox style zoom.
▪ Contact - Contact details and connection information
• About
• Bannered header
• Content appropriately formatted to subject
• Gallery
• Bannered header
• Each of the albums would have their own categorized image content
• Contact
• Bannered header
• Social Media connector available on all pages (like box, feed, etc) if applicable
• Content can be updated on all pages
• Basic Optimization for SEO with title tags, meta data where applicable.
• Google Analytics and Sitemap installed. (google account will be provided)
• Google Business Listing and Search Console Accounts created

Coded - Design and coding required

1 page

• Wordpress Responsive Design

```html
<!DOCTYPE html>
<html lang="en">
<head>
<meta charset="utf-8">
<title>Brookmoor Greens – Landscape Construction</title>
<link href="https://fonts.googleapis.com/css2?family=Kreon:wght@300;400;700&family=Open+Sans:wght@400;600;700&display=swap" rel="stylesheet">
<style>
:root{
  --green:#5e9a3a;
  --green-dark:#3f6f2a;
  --green-bar:#4c7d36;
  --ink:#1d1d1d;
  --night:#0f0f0f;
  --footer:#141414;
  --muted:#8a8a8a;
  --white:#ffffff;
  --line:#d9d9d9;
}
*{box-sizing:border-box;margin:0;padding:0}
html,body{width:1200px;height:3076px;overflow:hidden}
body{position:relative;font-family:"Open Sans",sans-serif;color:var(--ink);background:var(--white)}
a{color:inherit;text-decoration:none}

/* top bar */
.topbar{position:absolute;top:0;left:0;width:1200px;height:28px;background:var(--green-bar);color:var(--white);font-size:11px;display:flex;align-items:center;justify-content:space-between;padding:0 72px}
.topbar .dots{display:flex;gap:12px}
.dot{width:10px;height:10px;border-radius:50%;background:var(--white);display:block}
.topbar .contact-info{display:flex;gap:22px;align-items:center}
.topbar svg{vertical-align:-2px;margin-right:5px}

/* header */
.site-header{position:absolute;top:28px;left:0;width:1200px;height:60px;background:var(--white);display:flex;align-items:center;justify-content:space-between;padding:0 72px}
.brand{font-family:"Kreon",serif;font-size:28px;font-weight:400;color:var(--ink)}
.nav{display:flex;gap:40px;font-size:12px;font-weight:600;letter-spacing:.5px}
.nav a{padding:20px 0}
.nav a.active{color:var(--green);border-bottom:3px solid var(--green)}

/* hero */
.hero{position:absolute;top:88px;left:0;width:1200px;height:632px;background:linear-gradient(180deg,#5d6778 0%,#a58b74 28%,#c8a27c 38%,#56733d 58%,#2f5622 100%)}
.hero::after{content:"";position:absolute;inset:0;background:linear-gradient(90deg,rgba(0,0,0,.5) 0%,rgba(0,0,0,.15) 45%,rgba(0,0,0,0) 70%)}
.hero .social-rail{position:absolute;left:0;top:0;width:42px;height:100%;background:rgba(0,0,0,.55);z-index:2}
.social-rail span{position:absolute;left:50%;top:240px;transform:translateX(-50%) rotate(-90deg);transform-origin:center;white-space:nowrap;font-size:10px;color:var(--white);letter-spacing:2px}
.hero-copy{position:absolute;left:112px;top:222px;z-index:2;color:var(--white)}
.hero-copy .eyebrow{font-family:"Kreon",serif;font-size:30px;font-weight:300}
.hero-copy h1{font-family:"Kreon",serif;font-weight:400;font-size:72px;line-height:76px;margin-top:8px}
.btn{display:inline-block;font-size:10px;font-weight:700;letter-spacing:1px;padding:0 22px;height:40px;line-height:40px}
.btn-light{background:var(--white);color:var(--ink)}
.hero-copy .btn{margin-top:30px;height:46px;line-height:46px}
.slide-count{position:absolute;right:72px;top:520px;z-index:2;color:var(--white);font-size:12px;display:flex;align-items:baseline;gap:10px}
.slide-count b{font-size:30px;font-weight:700}

/* about */
.about{position:absolute;top:720px;left:0;width:1200px;height:470px;background:var(--night);overflow:hidden}
.about-photo{position:absolute;left:0;top:16px;width:560px;height:440px;background:linear-gradient(180deg,#8fa6bf 0%,#c9c6bb 40%,#5c8a3d 70%,#3f6c28 100%)}
.about-copy{position:absolute;left:612px;top:62px;width:500px;color:var(--white);z-index:1}
.about-copy .eyebrow{font-size:13px;letter-spacing:1px}
.about-copy h2{font-family:"Kreon",serif;font-weight:400;font-size:42px;margin-top:4px}
.about-copy h2 em,.section-title em{font-style:normal;color:var(--green)}
.about-copy p{font-size:13px;line-height:20px;margin-top:18px;color:#dcdcdc}
.about-copy .btn{margin-top:26px;height:44px;line-height:44px}
.watermark{position:absolute;font-family:"Kreon",serif;font-weight:700;letter-spacing:6px;white-space:nowrap}
.about .watermark{left:520px;bottom:-40px;font-size:140px;color:rgba(255,255,255,.05)}

/* services */
.services{position:absolute;top:1190px;left:0;width:1200px;height:440px;text-align:center}
.section-title{font-family:"Kreon",serif;font-weight:400;font-size:44px;color:var(--ink)}
.services .section-title{margin-top:70px}
.service-list{display:flex;justify-content:center;gap:120px;margin-top:46px}
.service{width:230px}
.service .icon{width:76px;height:76px;border:1px solid #cfcfcf;border-radius:50%;margin:0 auto;display:flex;align-items:center;justify-content:center}
.service h3{font-size:14px;font-weight:600;color:var(--green);margin-top:20px;letter-spacing:.5px}
.service p{font-size:11px;line-height:16px;color:#555;margin-top:8px}

/* gallery */
.gallery{position:absolute;top:1600px;left:0;width:1200px;height:560px;text-align:center}
.gallery .watermark{left:50%;top:-40px;transform:translateX(-50%);font-size:130px;color:rgba(0,0,0,.04)}
.gallery .section-title{position:relative;margin-top:0}
.gallery-grid{position:absolute;left:72px;top:82px;width:1056px;height:448px;display:grid;grid-template-columns:1fr 1fr 1fr;grid-template-rows:1fr 1fr;gap:22px}
.tile{position:relative}
.tile-a{background:linear-gradient(180deg,#9fb5cf 0%,#b7a58f 45%,#5f8a3f 75%,#3c6b27 100%)}
.tile-b{grid-row:1 / 3;grid-column:2;background:linear-gradient(180deg,#2a2d2a 0%,#3b4136 45%,#2a2c28 100%)}
.tile-c{background:linear-gradient(180deg,#c6d3e0 0%,#8ba971 45%,#4b7a30 100%)}
.tile-d{background:linear-gradient(180deg,#a6bed4 0%,#6c8a52 45%,#8a8a80 75%,#55703d 100%)}
.tile-e{background:linear-gradient(180deg,#d7dde4 0%,#6d9550 45%,#3e6e2a 100%)}
.tile-b .zoom{position:absolute;left:50%;top:50%;transform:translate(-50%,-50%)}

/* contact */
.contact{position:absolute;top:2210px;left:0;width:1200px;height:480px;background:radial-gradient(ellipse at 60% 40%,#4f7d3a 0%,#2f5526 55%,#1c3517 100%);color:var(--white);text-align:center}
.contact .section-title{color:var(--white);margin-top:40px}
.contact .section-title em{color:#8cc063}
.contact .lead{font-size:12px;margin-top:4px;color:#d8e4d0}
.contact-form{position:absolute;left:240px;top:150px;width:720px;text-align:left}
.field-row{display:flex;gap:40px}
.field{flex:1;border-bottom:1px solid rgba(255,255,255,.7);height:48px;padding-top:10px;font-size:11px}
.field.message{height:96px}
.submit{display:block;margin:34px auto 0;width:140px;height:40px;line-height:40px;background:var(--white);color:var(--ink);font-size:10px;font-weight:700;letter-spacing:1px;text-align:center}

/* footer */
.site-footer{position:absolute;top:2690px;left:0;width:1200px;height:386px;background:var(--footer);color:#cfcfcf}
.footer-cols{position:absolute;left:72px;top:40px;width:1056px;display:flex}
.footer-col h4{font-family:"Kreon",serif;font-weight:400;font-size:22px;color:var(--green);margin-bottom:16px}
.footer-brand{width:360px}
.footer-brand .brand{color:var(--white);font-size:26px}
.footer-brand p{font-size:11px;line-height:17px;margin-top:14px;width:250px}
.footer-social{display:flex;gap:10px;margin-top:20px}
.footer-social span{width:30px;height:30px;border:1px solid #777;border-radius:50%;display:flex;align-items:center;justify-content:center}
.footer-social span i{width:8px;height:8px;border-radius:50%;background:#ddd;display:block}
.quick{width:190px}
.quick li{list-style:none;font-size:11px;line-height:24px}
.contacts{width:240px}
.contacts li{list-style:none;font-size:11px;line-height:15px;display:flex;gap:10px;align-items:center;margin-bottom:12px}
.contacts .ico{width:22px;height:22px;border-radius:50%;background:var(--green);flex:none;display:flex;align-items:center;justify-content:center}
.newsletter{width:266px}
.newsletter .input{height:34px;background:var(--white);color:#999;font-size:10px;padding:0 10px;line-height:34px}
.newsletter .subscribe{height:34px;background:var(--green-dark);color:var(--white);font-size:10px;font-weight:700;letter-spacing:1px;text-align:center;line-height:34px;margin-top:6px}
.copyright{position:absolute;left:0;width:100%;top:308px;text-align:center;font-size:11px;color:#9a9a9a}
.copyright em{font-style:normal;color:var(--green)}
</style>
</head>
<body>

<div class="topbar">
  <div class="dots"><span class="dot"></span><span class="dot"></span><span class="dot"></span><span class="dot"></span></div>
  <div class="contact-info">
    <span><svg width="11" height="11" viewBox="0 0 24 24" fill="#fff"><path d="M6.6 10.8a15.1 15.1 0 0 0 6.6 6.6l2.2-2.2c.3-.3.7-.4 1-.2 1.1.4 2.3.6 3.6.6.6 0 1 .4 1 1V20c0 .6-.4 1-1 1A17 17 0 0 1 3 4c0-.6.4-1 1-1h3.5c.6 0 1 .4 1 1 0 1.3.2 2.5.6 3.6.1.3 0 .7-.2 1z"/></svg>555.014.2760</span>
    <span><svg width="12" height="10" viewBox="0 0 24 18" fill="none" stroke="#fff" stroke-width="2"><rect x="1" y="1" width="22" height="16"/><path d="M1 1l11 9 11-9"/></svg>info@brookmoorgreens.example</span>
  </div>
</div>

<header class="site-header">
  <div class="brand">Brookmoor Greens</div>
  <nav class="nav">
    <a class="active" href="#">HOME</a>
    <a href="#">ABOUT US</a>
    <a href="#">GALLERY</a>
    <a href="#">CONTACT US</a>
  </nav>
</header>

<section class="hero" role="img" aria-label="Photo of a grey shingled country house behind a wide green lawn and garden beds under a sunset sky">
  <div class="social-rail"><span>FOLLOW &nbsp;·&nbsp; LIKE &nbsp;·&nbsp; SHARE</span></div>
  <div class="hero-copy">
    <div class="eyebrow">Brookmoor Greens</div>
    <h1>Landscape<br>Construction</h1>
    <a class="btn btn-light" href="#">CONTACT US</a>
  </div>
  <div class="slide-count"><span>&larr; &rarr;</span><b>01</b><span>/03</span></div>
</section>

<section class="about">
  <div class="about-photo" role="img" aria-label="Photo of a white farmhouse with a wraparound porch, trees and a green lawn"></div>
  <div class="about-copy">
    <div class="eyebrow">WELCOME TO</div>
    <h2>Brookmoor <em>Greens</em></h2>
    <p>Brookmoor Greens is a full service landscape construction and maintenance company. We have been servicing the community for over 20 years and in that time have established ourselves as a premier contractor in the Hamptons. We pride ourselves on quality work and excellent customer service.</p>
    <a class="btn btn-light" href="#">BOOK NOW</a>
  </div>
  <div class="watermark">HISTORY</div>
</section>

<section class="services">
  <h2 class="section-title">Our Main <em>Services</em></h2>
  <div class="service-list">
    <div class="service">
      <div class="icon"><svg width="34" height="34" viewBox="0 0 34 34" fill="none" stroke="#5e9a3a" stroke-width="1.6"><path d="M17 4l6 14-6 12-6-12z"/><circle cx="17" cy="16" r="2.5"/><path d="M17 4v9"/></svg></div>
      <h3>DESIGN</h3>
      <p>Sed ut perspiciatis unde omnis iste natus error sit voluptatem accusantium doloremque</p>
    </div>
    <div class="service">
      <div class="icon"><svg width="34" height="34" viewBox="0 0 34 34" fill="none" stroke="#5e9a3a" stroke-width="1.6"><path d="M4 28L17 6l13 22z"/><path d="M11 28l6-10 6 10"/><circle cx="17" cy="14" r="1.5"/></svg></div>
      <h3>INSTALL</h3>
      <p>Sed ut perspiciatis unde omnis iste natus error sit voluptatem accusantium doloremque</p>
    </div>
    <div class="service">
      <div class="icon"><svg width="34" height="34" viewBox="0 0 34 34" fill="none" stroke="#5e9a3a" stroke-width="1.6"><path d="M6 28l14-14"/><path d="M18 8l8 8-4 4-8-8z"/><path d="M22 6l6 6"/></svg></div>
      <h3>MAINTAIN</h3>
      <p>Sed ut perspiciatis unde omnis iste natus error sit voluptatem accusantium doloremque</p>
    </div>
  </div>
</section>

<section class="gallery">
  <div class="watermark">GALLERY</div>
  <h2 class="section-title">Our <em>Gallery</em></h2>
  <div class="gallery-grid">
    <div class="tile tile-a" role="img" aria-label="Photo of a large stone and shingle house with a lawn"></div>
    <div class="tile tile-b" role="img" aria-label="Photo of a cobblestone driveway leading to a house at dusk">
      <svg class="zoom" width="26" height="26" viewBox="0 0 26 26" fill="none" stroke="#fff" stroke-width="2"><circle cx="11" cy="11" r="7"/><path d="M16 16l7 7M11 8v6M8 11h6"/></svg>
    </div>
    <div class="tile tile-c" role="img" aria-label="Photo of flowering trees beside a curved lawn"></div>
    <div class="tile tile-d" role="img" aria-label="Photo of a paved driveway curving past tall evergreens to a house"></div>
    <div class="tile tile-e" role="img" aria-label="Photo of a garden path with trimmed hedges leading to a white gate"></div>
  </div>
</section>

<section class="contact">
  <h2 class="section-title">Contact <em>Us</em></h2>
  <p class="lead">Sed ut perspiciatis unde omnis iste natus error sit voluptatem</p>
  <div class="contact-form">
    <div class="field-row">
      <div class="field">Name</div>
      <div class="field">Phone</div>
    </div>
    <div class="field">Email</div>
    <div class="field message">Message</div>
    <a class="submit" href="#">SUBMIT</a>
  </div>
</section>

<footer class="site-footer">
  <div class="footer-cols">
    <div class="footer-col footer-brand">
      <div class="brand">Brookmoor Greens</div>
      <p>At an early age, Jed Marlow began mowing lawns for local families. As he got older the number of lawn accounts began to grow.</p>
      <div class="footer-social"><span><i></i></span><span><i></i></span><span><i></i></span><span><i></i></span></div>
    </div>
    <div class="footer-col quick">
      <h4>Quick Links</h4>
      <ul><li>Home</li><li>About Us</li><li>Gallery</li><li>Contact Us</li></ul>
    </div>
    <div class="footer-col contacts">
      <h4>Contacts</h4>
      <ul>
        <li><span class="ico"><svg width="10" height="12" viewBox="0 0 10 14" fill="#fff"><path d="M5 0a5 5 0 0 0-5 5c0 4 5 9 5 9s5-5 5-9a5 5 0 0 0-5-5zm0 7a2 2 0 1 1 0-4 2 2 0 0 1 0 4z"/></svg></span>PO Box 318 • Elmhurst Vale<br>NY 10572</li>
        <li><span class="ico"><svg width="10" height="10" viewBox="0 0 24 24" fill="#fff"><path d="M6.6 10.8a15.1 15.1 0 0 0 6.6 6.6l2.2-2.2c.3-.3.7-.4 1-.2 1.1.4 2.3.6 3.6.6.6 0 1 .4 1 1V20c0 .6-.4 1-1 1A17 17 0 0 1 3 4c0-.6.4-1 1-1h3.5c.6 0 1 .4 1 1 0 1.3.2 2.5.6 3.6.1.3 0 .7-.2 1z"/></svg></span>555.014.2760</li>
        <li><span class="ico"><svg width="11" height="8" viewBox="0 0 24 18" fill="none" stroke="#fff" stroke-width="2.4"><rect x="1" y="1" width="22" height="16"/><path d="M1 1l11 9 11-9"/></svg></span>info@brookmoorgreens.example</li>
      </ul>
    </div>
    <div class="footer-col newsletter">
      <h4>Newsletter</h4>
      <div class="input">Enter Your Email</div>
      <div class="subscribe">SUBSCRIBE</div>
    </div>
  </div>
  <div class="copyright">Copyright © 2022 <em>Brookmoor Greens</em>. All Rights Reserved</div>
</footer>

</body>
</html>
```